Weddings by Liora
Wedding Planner
I NEED CONCEPTS WITH ENVELOPE, BUSINESS CARD AND PAPER...
NOT ONLY BUSINESS CARDS
THANK YOU
Hi everyone
thanks for sending.
please don't add Switzerland / schweiz...
i dont need to have the country on my business card. thanks a bunch. i am sorting out and get back to you now...
Designers: Logo .AI has been uploaded. Kindly refer to the creative brief. - Dean Pruitt
my logo should be there now....
thanks for drafts
plz upload the logo
My logo should be on business cards, letters and envelopes...
Writings should be same as used in my logo. Except if you add the address it should be kindof a "normal" writing.
i think it would look stupid if it will be same as in logo...
for questions, pls send message
cheers

```html
<!DOCTYPE html>
<html lang="en">
<head>
<meta charset="utf-8">
<title>Weddings by Liora – Stationery</title>
<link href="https://fonts.googleapis.com/css2?family=Lato:wght@300;400;700&display=swap" rel="stylesheet">
<style>
  :root{
    --bg:#e8e6e2;
    --paper:#ffffff;
    --gold:#c9972c;
    --black:#141414;
    --grey:#8f8b85;
    --ink:#3a3a3a;
    --rule:#e2e2e2;
  }
  *{box-sizing:border-box;margin:0;padding:0}
  html,body{width:1200px;height:1049px;overflow:hidden}
  body{background:var(--bg);font-family:'Lato',sans-serif;color:var(--ink);position:relative}

  .piece{position:absolute;background:var(--paper);box-shadow:0 3px 10px rgba(0,0,0,.18)}

  .brand{display:flex;align-items:center;gap:6px;color:var(--gold);font-weight:700;letter-spacing:.04em;white-space:nowrap}
  .brand-dot{width:10px;height:10px;border-radius:50%;background:var(--gold);flex:none}
  .brand--light{color:#fff}
  .brand--light .brand-dot{background:#fff}

  .contact{font-size:8px;line-height:1.55;color:var(--ink);border-left:1px solid var(--gold);padding-left:8px;white-space:nowrap}

  /* business cards */
  .card{width:210px;height:120px;padding:18px;display:flex;flex-direction:column;justify-content:center;align-items:center;gap:10px}
  .card .brand{font-size:13px}
  .card--white{justify-content:space-between;align-items:flex-start}
  .card--white .row{display:flex;justify-content:flex-end;width:100%}
  .card--gold{background:var(--gold)}
  .card--black{background:var(--black)}
  .card--grey{background:var(--grey)}
  .card-line{width:60px;height:1px;background:rgba(255,255,255,.6)}
  .card--black .card-line{background:var(--gold)}

  /* letterhead */
  .letterhead{left:700px;top:210px;width:460px;height:650px;padding:40px 40px 0;border-bottom:6px solid var(--gold)}
  .letterhead .brand{font-size:18px}
  .letterhead .contact{margin-top:14px}
  .decor{position:absolute;border-radius:50%;background:radial-gradient(ellipse at center,#ececec 0%,rgba(240,240,240,0) 70%)}
  .letterhead .decor{left:120px;top:260px;width:300px;height:300px}

  /* envelopes */
  .envelope{left:60px;width:560px;height:280px}
  .envelope--front{top:230px;padding:30px;border-bottom:5px solid var(--gold)}
  .envelope--front .brand{font-size:16px}
  .envelope--front .contact{margin-top:12px}
  .envelope--front .decor{left:280px;top:40px;width:220px;height:200px}
  .envelope--back{top:560px;overflow:hidden}
  .envelope--back svg{display:block}
  .envelope--back .brand{position:absolute;left:50%;top:52px;transform:translateX(-50%);font-size:14px}
</style>
</head>
<body>

  <div class="piece card card--white" style="left:60px;top:40px">
    <div class="brand"><span class="brand-dot"></span>Weddings by Liora</div>
    <div class="row">
      <div class="contact">Liora Vance<br>Wedding Planner<br>079 555 01 23<br>hello@lioravance.com<br>Rosenweg 8, 8001 Zurich</div>
    </div>
  </div>
  <div class="piece card card--gold" style="left:290px;top:40px">
    <div class="brand brand--light"><span class="brand-dot"></span>Weddings by Liora</div>
    <div class="card-line"></div>
  </div>
  <div class="piece card card--black" style="left:520px;top:40px">
    <div class="brand"><span class="brand-dot"></span>Weddings by Liora</div>
    <div class="card-line"></div>
  </div>
  <div class="piece card card--grey" style="left:750px;top:40px">
    <div class="brand brand--light"><span class="brand-dot"></span>Weddings by Liora</div>
    <div class="card-line"></div>
  </div>
  <div class="piece card card--white" style="left:940px;top:900px">
    <div class="brand"><span class="brand-dot"></span>Weddings by Liora</div>
    <div class="row">
      <div class="contact">Liora Vance<br>Wedding Planner<br>079 555 01 23<br>hello@lioravance.com<br>Rosenweg 8, 8001 Zurich</div>
    </div>
  </div>

  <div class="piece letterhead">
    <div class="decor" role="img" aria-label="Faint dove illustration"></div>
    <div class="brand"><span class="brand-dot"></span>Weddings by Liora</div>
    <div class="contact">Liora Vance<br>Wedding Planner<br>079 555 01 23<br>hello@lioravance.com<br>Rosenweg 8, 8001 Zurich</div>
  </div>

  <div class="piece envelope envelope--front">
    <div class="decor" role="img" aria-label="Faint dove illustration"></div>
    <div class="brand"><span class="brand-dot"></span>Weddings by Liora</div>
    <div class="contact">Liora Vance<br>Wedding Planner<br>079 555 01 23<br>hello@lioravance.com<br>Rosenweg 8, 8001 Zurich</div>
  </div>

  <div class="piece envelope envelope--back">
    <svg width="560" height="280" viewBox="0 0 560 280">
      <rect width="560" height="280" fill="#ffffff"/>
      <line x1="0" y1="280" x2="280" y2="150" stroke="#e2e2e2"/>
      <line x1="560" y1="280" x2="280" y2="150" stroke="#e2e2e2"/>
      <polygon points="0,0 560,0 560,20 280,150 0,20" fill="#ffffff" stroke="#e2e2e2"/>
      <polygon points="0,20 280,150 560,20 560,60 280,190 0,60" fill="#c9972c"/>
      <polygon points="0,60 280,190 560,60 560,95 280,225 0,95" fill="#141414"/>
    </svg>
    <div class="brand"><span class="brand-dot"></span>Weddings by Liora</div>
  </div>

</body>
</html>
```